Create a captivating door hanger for a holiday lighting company!

We need a beautiful 4.25x11 standard die cut door hanger that makes people want to call us or visit our website! It needs to be two-sided, in full color, with our logo, website, phone number, and a QR code (that goes to our website). We will provide the logo and one photo that must be used, but the rest is up to you. Our brand is sleek and sophisticated, but still warm and inviting.

Company Name: Brisbey Yuletide Glow
Website: www.brisbeyglow.example
Phone: 521.364.9087

Verbiage to incorporate

Tag line: "Shine Brightly this Season with Brisbey Yuletide Glow"

Why they should choose us:

Customized Designs: Our talented designers craft light displays that complement your style and architecture.

Professional Installation: Stay cozy indoors while we handle the heights and heavy lifting. Our experienced team will create a magical transformation!

Hassle-Free Storage: No more boxes taking up space... We carefully maintain and store our commercial-grade lights and make them ready to dazzle you again next year!

Call to Action: "Limited spots available. Reserve your light installation today!"

```html
<!DOCTYPE html>
<html lang="en">
<head>
<meta charset="utf-8">
<title>Brisbey Yuletide Glow – Door Hanger</title>
<link rel="stylesheet" href="https://fonts.googleapis.com/css2?family=Barlow+Condensed:wght@300;400;500;600;700&display=swap">
<style>
  :root {
    --backdrop: #bdbcb7;
    --navy: #0e141d;
    --gold: #d8c474;
    --gold-light: #e8db9c;
    --gold-deep: #b79f4f;
    --grey: #8d8d88;
    --white: #ffffff;
  }
  * { box-sizing: border-box; margin: 0; padding: 0; }
  html, body {
    width: 1200px; height: 1200px; overflow: hidden;
    background: var(--backdrop);
    font-family: "Barlow Condensed", "Arial Narrow", sans-serif;
  }
  .canvas { position: relative; width: 1200px; height: 1200px; }

  .hanger {
    position: absolute; top: 144px;
    width: 360px; height: 912px;
    background: var(--navy);
    border-radius: 34px;
    overflow: hidden;
    color: var(--gold);
    text-align: center;
  }
  .hanger--front { left: 190px; }
  .hanger--back { left: 650px; }

  .string-lights {
    position: absolute; left: 0; top: 0; width: 100%; height: 190px;
    background:
      radial-gradient(ellipse at 30% 20%, rgba(216,196,116,0.28), transparent 55%),
      radial-gradient(ellipse at 80% 40%, rgba(216,196,116,0.22), transparent 55%),
      linear-gradient(180deg, #1a1f26 0%, var(--navy) 100%);
  }
  .door-hole {
    position: absolute; left: 120px; top: 34px;
    width: 112px; height: 112px; border-radius: 50%;
    background: var(--backdrop);
  }

  /* Front side */
  .brand {
    position: absolute; left: 0; right: 0; top: 250px;
    display: flex; flex-direction: column; align-items: center; gap: 22px;
  }
  .brand__mark {
    width: 120px; height: 120px;
    border: 3px solid var(--gold);
  }
  .brand__name {
    font-weight: 300; font-size: 34px; line-height: 1.1;
    letter-spacing: 4px; text-transform: uppercase;
    color: var(--white);
  }
  .offer {
    position: absolute; left: 0; right: 0; top: 560px;
    line-height: 1.05;
  }
  .offer__note { font-size: 27px; font-weight: 400; color: var(--grey); letter-spacing: 1px; }
  .offer__lead { font-size: 36px; font-weight: 400; color: var(--gold-light); margin-top: 12px; }
  .offer__lead strong { font-weight: 700; display: block; font-size: 40px; margin: 4px 0; }
  .phone-band {
    position: absolute; left: 0; right: 0; top: 770px; height: 76px;
    background: var(--gold);
    color: var(--navy);
    font-weight: 700; font-size: 56px; line-height: 76px;
  }
  .site {
    font-weight: 700; font-size: 27px; color: var(--gold-light);
  }
  .hanger--front .site { position: absolute; left: 0; right: 0; top: 856px; }

  /* Back side */
  .why__title {
    position: absolute; left: 0; right: 0; top: 200px;
    font-weight: 300; font-size: 40px; letter-spacing: 1px;
    color: var(--gold);
  }
  .why__list {
    position: absolute; left: 0; right: 0; top: 262px;
    display: flex; flex-direction: column; gap: 18px;
  }
  .reason__heading {
    display: flex; align-items: center; gap: 10px;
    font-weight: 700; font-size: 17px; color: var(--gold-light);
    text-transform: uppercase; letter-spacing: 0.5px;
  }
  .reason__heading::before, .reason__heading::after {
    content: ""; flex: 1; height: 5px;
    border-top: 1px solid #4a4d52; border-bottom: 1px solid #4a4d52;
  }
  .reason__text {
    font-weight: 400; font-size: 14.5px; line-height: 1.25;
    color: var(--gold-light); padding: 2px 34px 0;
  }
  .house-photo {
    position: absolute; left: 0; right: 0; top: 520px; height: 314px;
    background:
      radial-gradient(ellipse at 50% 55%, rgba(240,220,150,0.75), transparent 60%),
      linear-gradient(180deg, var(--navy) 0%, #2a3240 30%, #6d6540 65%, #3f5a2a 100%);
  }
  .call-line {
    position: absolute; left: 0; right: 0; top: 786px;
    font-weight: 700; font-size: 30px; color: var(--white);
  }
  .hanger--back .site { position: absolute; left: 0; right: 0; top: 846px; }
</style>
</head>
<body>
<main class="canvas">

  <section class="hanger hanger--front" aria-label="Door hanger front">
    <div class="string-lights" role="img" aria-label="Gold string lights draped across the top"></div>
    <div class="door-hole"></div>
    <div class="brand">
      <div class="brand__mark"></div>
      <h1 class="brand__name">Brisbey<br>Yuletide Glow</h1>
    </div>
    <div class="offer">
      <p class="offer__note">Limited spots available.</p>
      <p class="offer__lead">Reserve your<strong>light installation</strong>today!</p>
    </div>
    <div class="phone-band">521.364.9087</div>
    <p class="site">www.brisbeyglow.example</p>
  </section>

  <section class="hanger hanger--back" aria-label="Door hanger back">
    <div class="string-lights" role="img" aria-label="Gold string lights draped across the top"></div>
    <div class="door-hole"></div>
    <h2 class="why__title">WHY CHOOSE US</h2>
    <div class="why__list">
      <article class="reason">
        <h3 class="reason__heading">Customized Designs</h3>
        <p class="reason__text">Our talented designers craft light displays that complement your style and architecture.</p>
      </article>
      <article class="reason">
        <h3 class="reason__heading">Professional Installation</h3>
        <p class="reason__text">Stay cozy indoors while we handle the heights and heavy lifting. Our experienced team will create a magical transformation!</p>
      </article>
      <article class="reason">
        <h3 class="reason__heading">Hassle-Free Storage</h3>
        <p class="reason__text">No more boxes taking up space...<br>We carefully maintain and store our commercial-grade lights and make them ready to dazzle you again next year!</p>
      </article>
    </div>
    <div class="house-photo" role="img" aria-label="Photo of a two-storey house outlined in warm white holiday lights at dusk"></div>
    <p class="call-line">Call Us Now 521.364.9087</p>
    <p class="site">www.brisbeyglow.example</p>
  </section>

</main>
</body>
</html>
```